Consulting company needs Business Cards - rough concept provided

I'm looking for someone to take our business card idea and make is slick and polished - to communicate our high-end, sophisticated, serious consulting business. We have a rough layout we did in-house. We are open to ideas on repo-ing elements, adjusting sizes, typefaces etc... within the general concept we've already come up with. We want it to be super-clean and sophisticated. We want to keep the white backgrounds, and blue brand colors. Our goal is to print with painted blue edges on thick cardstock. Thank you!!

```html
<!DOCTYPE html>
<html lang="en">
<head>
<meta charset="utf-8">
<title>Tall Harbor Business Cards</title>
<link href="https://fonts.googleapis.com/css2?family=Montserrat:wght@400;600;700&display=swap" rel="stylesheet">
<style>
  :root {
    --brand-blue: #009ddf;
    --ink: #1c1c1c;
    --muted-ink: #555555;
    --card: #ffffff;
    --backdrop: #cccccc;
  }
  * { margin: 0; padding: 0; box-sizing: border-box; }
  html, body {
    width: 1200px; height: 1200px; overflow: hidden;
    background: var(--backdrop);
    font-family: "Montserrat", sans-serif;
  }
  .sheet { position: relative; width: 1200px; height: 1200px; }
  .card {
    position: absolute; left: 248px; width: 704px; height: 449px;
    background: var(--card);
  }
  .card--front { top: 147px; }
  .card--back { top: 603px; height: 450px; }
  .accent-bar {
    position: absolute; left: 0; width: 21px; background: var(--brand-blue);
  }
  .card--front .accent-bar { top: 62px; height: 128px; }
  .card--back .accent-bar { top: 135px; height: 180px; }

  .wordmark {
    position: absolute; left: 44px; top: 62px;
    color: var(--brand-blue); font-weight: 700;
    font-size: 69px; line-height: 65px; letter-spacing: -1px;
  }
  .person { position: absolute; left: 50px; top: 258px; }
  .person__name {
    color: var(--brand-blue); font-weight: 600; font-size: 28px; line-height: 32px;
  }
  .person__role {
    color: var(--ink); font-weight: 400; font-size: 19px; line-height: 24px;
  }
  .contact {
    position: absolute; left: 442px; top: 327px;
    color: var(--ink); font-size: 16.5px; line-height: 24px; font-style: normal;
  }
  .positioning {
    position: absolute; left: 64px; top: 144px;
    color: var(--muted-ink); font-size: 28px; line-height: 40px; font-weight: 400;
  }
  .positioning strong { color: var(--brand-blue); font-weight: 700; }
</style>
</head>
<body>
  <main class="sheet">
    <section class="card card--front">
      <div class="accent-bar"></div>
      <h1 class="wordmark">TALL<br>HARBOR</h1>
      <div class="person">
        <p class="person__name">Dana Whitfield</p>
        <p class="person__role">Brand Consultant</p>
      </div>
      <address class="contact">
        4820 Maple Crest Ave, Ste 210<br>
        Linden Park, CA 94012<br>
        (555) 310 4721<br>
        dana@tallharbor.com
      </address>
    </section>
    <section class="card card--back">
      <div class="accent-bar"></div>
      <p class="positioning">
        <strong>We Help</strong> [target domographic] <strong>achieve</strong><br>
        [desired emotional outcome] <strong>by</strong> [our<br>
        unique approach] <strong>because</strong> [our brand<br>
        beliefs]
      </p>
    </section>
  </main>
</body>
</html>
```